Restaurant Email Club Sign Up Poster

Looking for a creative design that will catch people's eye and prompt them to sign up for our email club for our Restaurant that we run in Omaha, Nebraska. Open to any creative ways to most effectively grab peoples attention quickly without being too confusing. Want it to be simple but actionable.

Have attached some documents for your assistance - in addition to some marketing materials we have put out in the past.

Would like to put design on posters to hang up throughout the restaurant and likely will make stickers to put on check presenters as well.

Catchy stock photo or use of the cheese curd photo probably good idea - callout things mentioned in the "must haves" section below. Looking for most creative and catchy, yet simple design.

Target Market(s)

30-50 year olds males and females.

Industry/Entity Type

Restaurant

Requirements
Must have
• Must include callouts for -
• Sign up for E-Club for access to future offers and events (or something along these lines)
• Free Appetizer for Signing Up
• Free Birthday Meal
Should not have
• Please do not make this poster like the postcard that I attached to the project - this is not a poster to call out that we are a new burger and beer spot, that we have 40 rotating taps, or that we have 15 specialty burgers, etc. This is simply a poster to grab someones attention and get them to sign up for our email club. Should maybe have a catchy question, something like, "Want a Free Appetizer?" or something catchy and similar, and then below say "And access to future deals and event happenings?"

```html
<!DOCTYPE html>
<html lang="en">
<head>
<meta charset="utf-8">
<title>Get On The List – Prairie Tap Room E-Club</title>
<link rel="stylesheet" href="https://fonts.googleapis.com/css2?family=Archivo+Black&family=Archivo:wght@400;700;800&display=swap">
<style>
  :root {
    --backdrop: #3a3a3a;
    --paper: #ffffff;
    --brand-red: #ec1c24;
    --ink: #000000;
    --field-border: #9a9a9a;
    --field-text: #a3a3a3;
    --food-light: #f2b04a;
    --food-mid: #d9822b;
    --food-dark: #b05a1c;
  }
  * { box-sizing: border-box; margin: 0; padding: 0; }
  html, body {
    width: 1200px;
    height: 1200px;
    overflow: hidden;
    background: var(--backdrop);
  }
  .poster {
    position: absolute;
    left: 186px;
    top: 50px;
    width: 828px;
    height: 1100px;
    background: var(--paper);
    overflow: hidden;
  }
  .poster__band {
    position: absolute;
    left: 0; top: 0;
    width: 100%;
    height: 459px;
    background: var(--brand-red);
  }
  .headline {
    position: absolute;
    left: 0; top: 70px;
    width: 100%;
    text-align: center;
    color: var(--paper);
    font-family: "Archivo Black", "Arial Black", sans-serif;
    text-transform: uppercase;
  }
  .headline__lead {
    display: block;
    font-size: 92px;
    line-height: 1;
    letter-spacing: 0.01em;
  }
  .headline__main {
    display: block;
    font-size: 278px;
    line-height: 0.92;
    letter-spacing: -0.03em;
    margin-top: -4px;
  }
  .signup {
    position: absolute;
    left: 84px; top: 408px;
    width: 654px;
    height: 94px;
    display: flex;
  }
  .signup__field {
    flex: 1;
    background: var(--paper);
    border: 2px solid var(--field-border);
    border-right: none;
    display: flex;
    align-items: center;
    padding-left: 14px;
    font-family: "Archivo", Arial, sans-serif;
    font-weight: 400;
    font-size: 21px;
    color: var(--field-text);
    letter-spacing: 0.01em;
  }
  .signup__button {
    width: 198px;
    background: var(--ink);
    color: var(--paper);
    display: flex;
    align-items: center;
    justify-content: center;
    font-family: "Archivo Black", "Arial Black", sans-serif;
    font-size: 54px;
  }
  .food-photo {
    position: absolute;
    left: 84px; top: 594px;
    width: 680px;
    height: 220px;
    border-radius: 40px;
    background: radial-gradient(ellipse at 60% 45%, var(--food-light) 0%, var(--food-mid) 55%, var(--food-dark) 100%);
    opacity: 0.85;
  }
  .offer {
    position: absolute;
    left: 0; top: 842px;
    width: 100%;
    text-align: center;
    text-transform: uppercase;
  }
  .offer__intro {
    font-family: "Archivo", Arial, sans-serif;
    font-weight: 800;
    font-size: 23px;
    line-height: 30px;
    color: var(--ink);
  }
  .offer__perks {
    margin-top: 10px;
    font-family: "Archivo Black", "Arial Black", sans-serif;
    font-size: 44px;
    line-height: 52px;
    color: var(--brand-red);
  }
  .brand {
    position: absolute;
    left: 0; top: 1010px;
    width: 100%;
    display: flex;
    align-items: center;
    justify-content: center;
    gap: 14px;
    font-family: "Archivo Black", "Arial Black", sans-serif;
    font-size: 30px;
    color: var(--ink);
    text-transform: uppercase;
  }
  .brand__mark {
    width: 26px;
    height: 26px;
    background: var(--ink);
  }
  .fine-print {
    position: absolute;
    left: 0; top: 1074px;
    width: 100%;
    text-align: center;
    font-family: "Archivo", Arial, sans-serif;
    font-weight: 400;
    font-size: 8.5px;
    color: var(--ink);
    text-transform: uppercase;
  }
</style>
</head>
<body>
  <main class="poster">
    <div class="poster__band"></div>

    <h1 class="headline">
      <span class="headline__lead">Get on the</span>
      <span class="headline__main">List</span>
    </h1>

    <div class="signup">
      <div class="signup__field">YOURHUNGRY@PRAIRIETAPROOM.COM</div>
      <div class="signup__button">JOIN</div>
    </div>

    <div class="food-photo" role="img" aria-label="Photo of golden fried cheese curds, one broken open with melted cheese"></div>

    <section class="offer">
      <p class="offer__intro">Join our e-club for<br>exclusive offers and events</p>
      <p class="offer__perks">Free appetizer<br>Free birthday meal</p>
    </section>

    <div class="brand">
      <span class="brand__mark"></span>
      <span class="brand__name">Prairie Tap Room</span>
    </div>

    <p class="fine-print">Must be 21 years of age. Some restrictions apply. Must sign up 10 days prior to your birthday to receive offer.</p>
  </main>
</body>
</html>
```